New design for Vel Hart [Plonix]

I manage a small web hosting company that I have been doing for many years, and I have quite a few clients that have been with me for a long time. A lot of them have extremely outdated websites such as the one this project is for " www.velhart.com.au ". I am transferring all my clients over to Plonix white-label. The website is very basic, it's only a small amount of links and a contact form.
I need a design that is up-to-date and attractive for today's standards, and of course plonix compatible.
Thanks
Industry/Entity Type
It Company
Look and feel
Each slider illustrates characteristics of the customer's brand and the style your logo design should communicate.

```html
<!DOCTYPE html>
<html lang="en">
<head>
<meta charset="utf-8">
<title>Vel Hart – Generator Services</title>
<link rel="stylesheet" href="https://fonts.googleapis.com/css2?family=PT+Sans:wght@400;700&family=Open+Sans:wght@400;600&family=Arimo:wght@400;700&display=swap">
<style>
  :root {
    --blue: #0a4f9c;
    --blue-dark: #073b78;
    --blue-light: #1a66b8;
    --red: #e3000f;
    --red-text: #c8101d;
    --grey-panel: #d9dadc;
    --grey-soft: #e8e8e9;
    --text: #333333;
    --white: #ffffff;
  }
  * { box-sizing: border-box; margin: 0; padding: 0; }
  html, body { width: 1125px; height: 1200px; overflow: hidden; background: var(--white); }
  body { position: relative; font-family: "PT Sans", sans-serif; color: var(--text); }
  .abs { position: absolute; }

  .site-header { left: 0; top: 0; width: 1125px; height: 119px;
    background: linear-gradient(#f8f8f8, #ffffff 40%, #eeeeee); }
  .brand { left: 110px; top: 34px; display: flex; align-items: center; gap: 10px;
    font-family: "PT Sans", sans-serif; font-weight: 700; font-size: 34px; color: var(--red-text); }
  .brand-dot { width: 16px; height: 16px; border-radius: 50%; background: var(--blue); }
  .header-vehicle { left: 790px; top: 38px; width: 275px; height: 72px; border-radius: 10px;
    background: linear-gradient(#f4f4f4, #bfc3c8); }

  .main-nav { left: 0; top: 119px; width: 1125px; height: 41px;
    background: linear-gradient(var(--blue-light), var(--blue-dark)); border-bottom: 4px solid var(--red); }
  .main-nav a { position: absolute; top: 12px; color: var(--white); text-decoration: none;
    font-weight: 700; font-size: 14px; }
  .nav-active { left: 196px; top: 122px; width: 83px; height: 38px; background: var(--red);
    border-radius: 6px 6px 0 0; }
  .dropdown { left: 196px; top: 148px; width: 165px; height: 92px; background: var(--red); z-index: 3;
    padding: 18px 0 0 9px; }
  .dropdown li { list-style: none; color: var(--white); font-weight: 700; font-size: 12px; height: 21px; }
  .dropdown li span { font-size: 9px; margin-right: 8px; }

  .slider-frame { left: 71px; top: 166px; width: 973px; height: 410px; background: var(--grey-panel); }
  .slider-shadow { left: 80px; top: 576px; width: 955px; height: 22px;
    background: radial-gradient(ellipse at 50% 0, rgba(0,0,0,.35), rgba(0,0,0,0) 70%); }
  .slide-photo { left: 81px; top: 176px; width: 951px; height: 367px;
    background: linear-gradient(100deg, #4a3a1c 0%, #c9a422 30%, #d4b230 48%, #6a5a3a 62%, #b8501f 80%, #8d8f94 100%); }
  .slide-caption { left: 117px; top: 482px; font-family: "Open Sans", sans-serif; font-size: 21px;
    color: var(--white); letter-spacing: -0.5px; text-shadow: 0 0 3px #0b2a55, 0 0 2px #0b2a55; z-index: 2; }
  .slide-dots { left: 537px; top: 551px; display: flex; gap: 4px; }
  .slide-dots i { width: 16px; height: 16px; border-radius: 50%;
    background: radial-gradient(circle at 40% 35%, #8fd0f5, #1b7fc7 70%); }
  .slide-dots i.on { background: radial-gradient(circle at 40% 35%, #ff8a7a, #d40a0a 70%); }
  .slide-arrow { top: 344px; width: 54px; height: 54px; border-radius: 50%; background: var(--white);
    box-shadow: 0 1px 3px rgba(0,0,0,.3); display: flex; align-items: center; justify-content: center; z-index: 2; }

  .service-tile { top: 607px; width: 229px; height: 188px; background: var(--blue); padding: 3px; }
  .tile-photo { width: 223px; height: 152px; }
  .tile-label { height: 30px; display: flex; align-items: center; justify-content: flex-end; gap: 10px;
    padding-right: 12px; color: var(--white); font-weight: 700; font-size: 15px; }

  .panel { top: 814px; height: 236px; border-radius: 6px 6px 0 0;
    background: linear-gradient(#d6d6d6, #f0f0f0 55%, #ffffff); }
  .panel-title { font-family: "Open Sans", sans-serif; color: var(--red-text); }
  .rule { border-bottom: 2px dotted #555; }
  .login-label { font-family: "Arimo", sans-serif; font-size: 14px; color: #222; }
  .field { width: 128px; height: 24px; border: 1px solid #888; background: #f5f5f5; }
  .submit-btn { left: 197px; top: 979px; width: 75px; height: 28px; border-radius: 5px; background: var(--red);
    color: var(--white); font-family: "Arimo", sans-serif; font-size: 14px; padding: 5px 0 0 11px; }
  .welcome-text { left: 406px; top: 888px; width: 615px; font-size: 15px; line-height: 24px; letter-spacing: .2px; }
  .welcome-text p + p { margin-top: 24px; }

  .site-footer { left: 0; top: 1085px; width: 1125px; height: 115px;
    background: linear-gradient(var(--blue), var(--blue-dark)); font-family: "Arimo", sans-serif; color: var(--white); }
  .social { display: flex; gap: 13px; }
  .social i { width: 26px; height: 26px; border-radius: 50%; background: #5d93cf; box-shadow: 0 1px 2px rgba(0,0,0,.4); }
</style>
</head>
<body>
  <header class="abs site-header"></header>
  <div class="abs brand"><span>Vel Hart</span><span class="brand-dot"></span></div>
  <div class="abs header-vehicle" role="img" aria-label="White company service utility vehicle"></div>

  <nav class="abs main-nav">
    <a style="left:130px">Home</a>
    <a style="left:302px">Products and Services</a>
    <a style="left:484px">Projects &amp; Clients</a>
    <a style="left:639px">What's New</a>
    <a style="left:757px">Contact Us</a>
    <a style="left:865px">Site Map</a>
  </nav>
  <div class="abs nav-active"><span style="position:absolute;left:10px;top:9px;color:#fff;font-weight:700;font-size:14px">About Us</span></div>
  <ul class="abs dropdown">
    <li><span>&gt;&gt;</span>Company History</li>
    <li><span>&gt;&gt;</span>Company Philosophy</li>
    <li><span>&gt;&gt;</span>Company Management</li>
  </ul>

  <div class="abs slider-frame"></div>
  <div class="abs slider-shadow"></div>
  <div class="abs slide-photo" role="img" aria-label="Yellow diesel generator engine in a plant room"></div>
  <div class="abs slide-caption">Lorem ipsum dolor sit amet, consectetuer adipiscing elit.Lorem ipsum dolor sit amet, adipiscing &nbsp;elit</div>
  <div class="abs slide-dots"><i class="on"></i><i></i><i></i><i></i></div>
  <div class="abs slide-arrow" style="left:46px;justify-content:flex-end;padding-right:12px">
    <svg width="16" height="14" viewBox="0 0 16 14"><path d="M1 1l6 6-6 6M8 1l6 6-6 6" fill="none" stroke="#333" stroke-width="2.5"/></svg>
  </div>
  <div class="abs slide-arrow" style="left:1015px;justify-content:flex-start;padding-left:12px">
    <svg width="16" height="14" viewBox="0 0 16 14"><path d="M15 1l-6 6 6 6M8 1L2 7l6 6" fill="none" stroke="#333" stroke-width="2.5"/></svg>
  </div>

  <div class="abs service-tile" style="left:78px">
    <div class="tile-photo" role="img" aria-label="Blue generator set in an engine room" style="background:linear-gradient(#9aa0a8,#2c4f86 60%,#4a4a4a)"></div>
    <div class="tile-label">Generator Sets <svg width="10" height="14"><path d="M2 1l6 6-6 6" fill="none" stroke="#9cc8f0" stroke-width="2.5"/></svg></div>
  </div>
  <div class="abs service-tile" style="left:322px">
    <div class="tile-photo" role="img" aria-label="Generator control panels and PLC cabinets" style="background:linear-gradient(90deg,#b9b8ae,#d8d6cc 50%,#a89c86)"></div>
    <div class="tile-label">Controls &amp; PLC's <svg width="10" height="14"><path d="M2 1l6 6-6 6" fill="none" stroke="#9cc8f0" stroke-width="2.5"/></svg></div>
  </div>
  <div class="abs service-tile" style="left:565px">
    <div class="tile-photo" role="img" aria-label="Metal acoustic enclosure with a service vehicle" style="background:linear-gradient(#8a6050,#b8bcc2 25%,#d6d8da 70%,#9a9a98)"></div>
    <div class="tile-label">Acoustic Enclosures <svg width="10" height="14"><path d="M2 1l6 6-6 6" fill="none" stroke="#9cc8f0" stroke-width="2.5"/></svg></div>
  </div>
  <div class="abs service-tile" style="left:810px">
    <div class="tile-photo" role="img" aria-label="Generator being lifted by crane on a project site" style="background:linear-gradient(#9fb8cf,#c9d6e2 60%,#606468)"></div>
    <div class="tile-label">Current Projects <svg width="10" height="14"><path d="M2 1l6 6-6 6" fill="none" stroke="#9cc8f0" stroke-width="2.5"/></svg></div>
  </div>

  <section class="abs panel" style="left:81px;width:288px">
    <h2 class="abs panel-title" style="left:35px;top:13px;font-size:19px;font-weight:400">Login</h2>
    <div class="abs rule" style="left:3px;top:41px;width:282px"></div>
    <span class="abs login-label" style="left:21px;top:70px">User Name&nbsp; :</span>
    <div class="abs field" style="left:111px;top:69px"></div>
    <span class="abs login-label" style="left:30px;top:118px">Password&nbsp; :</span>
    <div class="abs field" style="left:111px;top:118px"></div>
  </section>
  <div class="abs submit-btn">Submit</div>

  <section class="abs panel" style="left:383px;width:657px">
    <h1 class="abs panel-title" style="left:31px;top:14px;font-size:25px;font-weight:400;letter-spacing:-0.3px">Welcome to Vel Hart</h1>
    <div class="abs rule" style="left:31px;top:51px;width:298px"></div>
  </section>
  <div class="abs welcome-text">
    <p>VelHart Pty Ltd was formed in November 1996 with the aim of being able to offer a complete Generator (System) Service.</p>
    <p>VelHart's Management and Staff have been involved in the generator industry (ex Ironcat &amp; Kumbrell dealer personnel) for over 30 years. During this time having direct involvement with Prime, Standby, Diesel and Gas applications.</p>
  </div>

  <footer class="abs site-footer">
    <span class="abs" style="left:121px;top:19px;font-size:14px">Connect With Us</span>
    <div class="abs social" style="left:121px;top:62px"><i></i><i></i><i></i><i></i></div>
    <span class="abs" style="left:527px;top:32px;font-size:12px;word-spacing:1px">Privacy Policy &nbsp;&nbsp; | &nbsp;&nbsp; Terms &amp; Conditions &nbsp;&nbsp; | &nbsp;&nbsp; Contact Us</span>
    <span class="abs" style="left:585px;top:70px;font-size:12px">© 2011 velhart, All Rights Reserved</span>
  </footer>
</body>
</html>
```